RM Tomás Rivera (Business Card)

Hi designers, in this work, I'm looking for an sophisticated stylish, elegant and proffesional personal card. We have a laboratory of pathology automated, with equipments high quality.
In this web the designers, have created my business logo, the name is "RM Tomás Rivera"
In our lab, we principal work is to prepare the biopsies for further diagnostic of diseases like cancer, tumors, etc.
I need that the first face, only having my complete logo (Rm Tomás Rivera, Laboratorio de procesamiento Histologico)
The overleaf, could repeat the same logo, like water logo.
In this face, I need to say: My full data:

Técnico en Anatomía Patológica
Tomás Rivera Ibarra M.P 47203
Av. Paredes Luján 418 - 2do piso - Instituto Marbel.
Córdoba, Argentina
(0351) 154820937
rivera.tomas@correolab.example

with respect the colors of card, use your imagination, the original logo color is violet, I haven't chosen a color base for the card.

attached pictures are examples of cards I like your DESIGN.
Attached too, the original logo to my company.

the size of card are:
horizontal: 9cm
vertical: 5,5cm

any question that you have, not doubt to question me,
Hand to work!

Industry/Entity Type

Laboratory

Requirements
Must have
• designers sophisticated, not simples, like show the images attached

```html
<!DOCTYPE html>
<html lang="es">
<head>
<meta charset="utf-8">
<title>RM Tomás Rivera — Tarjeta personal</title>
<link rel="stylesheet" href="https://fonts.googleapis.com/css2?family=Josefin+Sans:wght@300&family=Oswald:wght@400&family=Mulish:wght@700;800&display=swap">
<style>
  :root {
    --violet-deep: #4f2a6e;
    --violet-mid: #62387f;
    --violet-glow: #7a4e98;
    --paper: #ffffff;
    --paper-edge: #e4e3e6;
    --ink-violet: #4a2a66;
    --ink-grey: #707070;
    --page: #ece9ef;
    --white: #ffffff;
  }
  html, body {
    margin: 0;
    padding: 0;
    width: 1200px;
    height: 1181px;
    overflow: hidden;
    background: var(--page);
  }
  .canvas {
    position: relative;
    width: 1200px;
    height: 1181px;
  }
  .card {
    position: absolute;
    left: 208px;
    width: 784px;
    height: 452px;
    border-radius: 30px;
    overflow: hidden;
    box-shadow: 0 6px 14px rgba(40, 20, 60, 0.25);
  }
  /* Front */
  .card--front {
    top: 103px;
    background: radial-gradient(ellipse 60% 70% at 50% 50%, var(--violet-glow) 0%, var(--violet-mid) 45%, var(--violet-deep) 100%);
  }
  .brand {
    position: absolute;
    left: 0;
    right: 0;
    top: 270px;
    text-align: center;
    color: var(--white);
  }
  .brand__mark {
    position: absolute;
    left: 150px;
    width: 484px;
    top: 130px;
    margin: 0;
    font-family: "Josefin Sans", sans-serif;
    font-weight: 300;
    font-size: 40px;
    letter-spacing: 6px;
    text-transform: uppercase;
    text-align: center;
    color: var(--white);
  }
  .brand__rule {
    position: absolute;
    left: 200px;
    width: 379px;
    top: 262px;
    height: 2px;
    background: var(--white);
  }
  .brand__tagline {
    position: absolute;
    left: 0;
    right: 0;
    top: 268px;
    margin: 0;
    font-family: "Oswald", sans-serif;
    font-weight: 400;
    font-size: 26px;
    letter-spacing: -0.3px;
    text-align: center;
    color: var(--white);
  }
  /* Back */
  .card--back {
    top: 617px;
    background: var(--violet-mid);
  }
  .band {
    position: absolute;
    left: 0;
    right: 0;
    background: radial-gradient(ellipse 55% 160% at 50% 50%, var(--violet-glow) 0%, var(--violet-deep) 100%);
  }
  .band--top { top: 0; height: 54px; }
  .band--bottom { top: 395px; height: 57px; }
  .sheet {
    position: absolute;
    left: 0;
    right: 0;
    top: 54px;
    height: 341px;
    background: radial-gradient(ellipse 60% 70% at 50% 55%, var(--paper) 0%, var(--paper) 35%, var(--paper-edge) 100%);
  }
  .sheet__watermark {
    position: absolute;
    left: 322px;
    top: 80px;
    width: 140px;
    height: 140px;
    border-radius: 50%;
    background: var(--ink-violet);
    opacity: 0.06;
  }
  .identity {
    position: absolute;
    left: 0;
    right: 0;
    top: 140px;
    text-align: center;
  }
  .identity__name {
    margin: 0;
    font-family: "Mulish", sans-serif;
    font-weight: 800;
    font-size: 26px;
    line-height: 32px;
    color: var(--ink-violet);
  }
  .identity__name .surname { color: var(--ink-grey); }
  .identity__role {
    margin: 0;
    font-family: "Mulish", sans-serif;
    font-weight: 800;
    font-size: 16px;
    line-height: 22px;
    color: var(--ink-violet);
  }
  .contact {
    position: absolute;
    top: 280px;
    font-family: "Mulish", sans-serif;
    font-weight: 700;
    font-size: 11.5px;
    line-height: 15px;
    color: var(--ink-violet);
    margin: 0;
    font-style: normal;
  }
  .contact--address {
    right: 403px;
    text-align: right;
  }
  .contact--reach {
    left: 406px;
    text-align: left;
  }
  .contact__divider {
    position: absolute;
    left: 393px;
    top: 274px;
    width: 2px;
    height: 56px;
    background: var(--ink-violet);
  }
</style>
</head>
<body>
<main class="canvas">
  <section class="card card--front" aria-label="Frente de la tarjeta">
    <p class="brand__mark">RM Tomás Rivera</p>
    <div class="brand__rule"></div>
    <p class="brand__tagline">LABORATORIO DE PROCESAMIENTO HISTOLOGICO</p>
  </section>

  <section class="card card--back" aria-label="Dorso de la tarjeta">
    <div class="band band--top"></div>
    <div class="sheet">
      <div class="sheet__watermark"></div>
      <div class="identity">
        <h1 class="identity__name">Tomás <span class="surname">Rivera</span> Ibarra</h1>
        <p class="identity__role">Técnico en Anatomía Patológica</p>
      </div>
      <address class="contact contact--address">
        Av. Paredes Luján 418<br>
        2do piso - Instituto Marbel<br>
        Córdoba, Argentina
      </address>
      <div class="contact__divider"></div>
      <p class="contact contact--reach">
        (0351) 154820937<br>
        rivera.tomas@correolab.example<br>
        M.P 47203
      </p>
    </div>
    <div class="band band--bottom"></div>
  </section>
</main>
</body>
</html>
```